Why engage Insight Harbor?

We are starting a new company that will perform usability consulting and offer usability lab rental. We are in need a one page description flyer.
Updates

Wow! We saw some very interesting and creative flyers posted for review in our contest.

Unfortunately, my schedule became a bit crazy and I may not get back to evaluating them until next week :(  In the meantime, I did want to say thank you for your entries!

Cheers!
Marla

Target Market(s)

product designers, human factors/usability researchers, consumer researcher firms, etc

Industry/Entity Type

It Company

Requirements
Must have
• We would like to see designs with a simple, yet modern, sophisticated feel. I will include our logo images that need to be incorporated along with the font used.

The file called flyer.pdf has all of the information that needs to be included.

Please include 1-3 appropriate stock photos. Please see text in flyer.pdf for description of our services.

Nice to have
• Additionally, there is a sample flyer design that we like for reference. Not a requirement...it is just a reference for the kind of style that we are looking for.

```html
<!DOCTYPE html>
<html lang="en">
<head>
<meta charset="utf-8">
<title>Why Choose Insight Harbor?</title>
<link href="https://fonts.googleapis.com/css2?family=Roboto:wght@100;300;400&display=swap" rel="stylesheet">
<style>
  :root {
    --green: #8cc63f;
    --navy: #1b3a6b;
    --title-dark: #3f5a32;
    --text: #4a4a4a;
    --muted: #5f5f5f;
    --paper: #ffffff;
    --photo-dark: #2a2620;
  }
  * { box-sizing: border-box; margin: 0; padding: 0; }
  html, body { width: 849px; height: 1200px; overflow: hidden; background: var(--paper); }
  body { font-family: "Roboto", Arial, sans-serif; color: var(--text); }
  .flyer { position: relative; width: 849px; height: 1200px; overflow: hidden; background: var(--paper); }

  .hero-photo { position: absolute; left: 0; top: 0; width: 849px; height: 440px; }
  .green-band { position: absolute; left: 0; top: 0; width: 849px; height: 440px; }

  .brand { position: absolute; left: 38px; top: 42px; }
  .brand-name { display: flex; align-items: center; gap: 10px; font-size: 34px; font-weight: 300; color: var(--navy); letter-spacing: 1px; line-height: 1; }
  .brand-dot { width: 14px; height: 14px; border-radius: 50%; background: var(--green); }
  .brand-address { margin-top: 10px; font-size: 12.5px; color: var(--navy); }

  .headline { position: absolute; left: 36px; top: 184px; font-weight: 100; line-height: 1; }
  .headline .line-1 { display: block; font-size: 60px; color: var(--title-dark); letter-spacing: -1px; }
  .headline .line-2 { display: block; font-size: 36px; margin-top: 4px; color: #fff; font-weight: 300; }
  .headline .line-2 span { color: var(--navy); }

  .intro { position: absolute; left: 36px; top: 294px; width: 600px; font-size: 13.6px; font-weight: 300; line-height: 19px; color: #2f3a2a; }
  .intro p + p { margin-top: 4px; }

  .feature { position: absolute; width: 330px; }
  .feature.left { left: 33px; }
  .feature.right { left: 410px; width: 331px; }
  .feature h2 { font-size: 14.5px; font-weight: 400; color: var(--navy); text-transform: uppercase; margin-bottom: 6px; letter-spacing: .2px; line-height: 17px; }
  .feature p { font-size: 12.2px; font-weight: 300; line-height: 18px; color: var(--muted); text-align: justify; }

  .bottom-photo { position: absolute; left: 0; top: 893px; width: 849px; height: 249px; }

  .contact { position: absolute; left: 0; top: 1148px; width: 849px; text-align: center; font-size: 23px; font-weight: 300; color: #3c3c3c; }
  .contact .divider { color: var(--green); margin: 0 6px; }
</style>
</head>
<body>
<div class="flyer">
  <svg class="hero-photo" role="img" aria-label="Photo of a senior man at a white desk testing a handheld medical device" viewBox="0 0 849 440">
    <defs>
      <linearGradient id="roomLight" x1="0" y1="0" x2="1" y2="1">
        <stop offset="0" stop-color="#ffffff"/>
        <stop offset="1" stop-color="#e6eaec"/>
      </linearGradient>
      <radialGradient id="figure" cx=".5" cy=".4" r=".5">
        <stop offset="0" stop-color="#d9dcdc"/>
        <stop offset="1" stop-color="#eef1f2" stop-opacity="0"/>
      </radialGradient>
    </defs>
    <rect width="849" height="440" fill="url(#roomLight)"/>
    <ellipse cx="640" cy="200" rx="220" ry="200" fill="url(#figure)"/>
  </svg>

  <svg class="green-band" viewBox="0 0 849 440" aria-hidden="true">
    <polygon points="0,146 432,146 770,430 0,430" fill="var(--green)"/>
  </svg>

  <div class="brand">
    <div class="brand-name"><span class="brand-dot"></span>INSIGHT HARBOR</div>
    <div class="brand-address">2140 W. Canyon Ridge Way Tempe, AZ 85281</div>
  </div>

  <h1 class="headline">
    <span class="line-1">WHY CHOOSE</span>
    <span class="line-2">INSIGHT <span>HARBOR?</span></span>
  </h1>

  <div class="intro">
    <p>We are a network of human Factors engineers, usability specialists, and cognitive/consumer psychologists, who help you design and evaluate the usefulness, usability and desirability of your products.</p>
    <p>Lease our state of the art consumer research and usability lab, or partner with us on usability testing, eye-tracking studies, participatory design, online survey research, ethnographic studies, focus groups and more.</p>
  </div>

  <div class="feature left" style="top:451px">
    <h2>Experience</h2>
    <p>Founded by a Professor of Cognitive Psychology and Human Factors with over twenty years of experience, our group includes MS and PhD level consultants with experience working for and consulting with companies like Brightline, Corvana, Helixa Medical, Veracor, Summit Care Hospitals, Aldridge and Hale, Quantiva, and Starfield Studios.</p>
  </div>
  <div class="feature left" style="top:585px">
    <h2>Range of Products and Industries</h2>
    <p>Our consultants have extensive experience in design and evaluation of computing, web, tablet, smart phone, product, medical, consumer, and many other types of products and user interfaces.</p>
  </div>
  <div class="feature left" style="top:683px">
    <h2>Recruiting</h2>
    <p>Sizable database with ability to recruit research participants according to age, sex, occupation, health status, and other parameters.</p>
  </div>
  <div class="feature left" style="top:766px">
    <h2>Accessibility</h2>
    <p>Located on the first floor, with ample, free, convenient and handicap parking. Adjustable artificial and natural lighting.</p>
  </div>
  <div class="feature left" style="top:835px">
    <h2>Audio/Video</h2>
    <p>On-site video editing. Highlight video included in facility rental.</p>
  </div>

  <div class="feature right" style="top:451px">
    <h2>Service</h2>
    <p>Full range of consumer research and usability services, including ethnography, participatory design, questionnaires, user diaries, usability testing, usability evaluation, card sorting, psychometric scaling, focus groups and more.</p>
  </div>
  <div class="feature right" style="top:585px">
    <h2>Onsite or Remote Streaming Video</h2>
    <p>Sessions can be viewed in many ways: Through our observation mirror, in our meeting room via pan-tilt- zoom camera, at your site on your computer, on your tablet or phone.</p>
  </div>
  <div class="feature right" style="top:683px">
    <h2>Client Service Specialist</h2>
    <p>Need copies, printing, lunch, or dinner reservations? Our client service specialist will make sure you have everything you need.</p>
  </div>
  <div class="feature right" style="top:767px">
    <h2>Office Space</h2>
    <p>Meeting room for work, phone calls and conference calls. Wireless Internet.</p>
  </div>
  <div class="feature right" style="top:834px">
    <h2>Transcription</h2>
    <p>Transcription services and word frequency key-words-in-context, and word co-occurrence analyses available</p>
  </div>
  <div class="feature right" style="top:902px">
    <h2>Bilingual</h2>
    <p>Several consultants fluent in both English and Spanish</p>
  </div>

  <svg class="bottom-photo" role="img" aria-label="Photo of a dim conference room with a large wall screen and a person seated at the table" viewBox="0 0 849 249">
    <defs>
      <linearGradient id="room" x1="0" y1="0" x2="0" y2="1">
        <stop offset="0" stop-color="#8a8272"/>
        <stop offset=".55" stop-color="#4a4236"/>
        <stop offset="1" stop-color="var(--photo-dark)"/>
      </linearGradient>
    </defs>
    <rect x="0" y="62" width="849" height="187" fill="url(#room)"/>
    <rect x="85" y="0" width="236" height="165" fill="#0d0d0d"/>
  </svg>

  <div class="contact">602.555.0147<span class="divider">|</span>www.insightharborlab.com</div>
</div>
</body>
</html>
```